Web Site Design and Business Card design for Recruiting Company

There are three major tasks in this project:
1) I need to re-design my newly created website www.talvenhire.net using the same logo but creating a totally different recruiting template that will apply better for a recruitment site. I want to use the elements of the Talvenhire Network logo (which is the road junction) and red, black and gray colors throughout the website. I need someone to both design and launch the site...
2) I would also like to design a double sided business card using the same logo/colors and elements as described above
3) I would also like to have a small thumbnail logo created. As our large logo cannot be previewed easily on the Corvanet or on Pellmark Orbit tab images

The design should be contemporary, minimalist and slick

```html
<!DOCTYPE html>
<html lang="en">
<head>
<meta charset="utf-8">
<title>Talvenhire Network</title>
<link href="https://fonts.googleapis.com/css2?family=Lato:wght@400;700;900&display=swap" rel="stylesheet">
<style>
:root{
  --red:#ec1c24;
  --red-dark:#c8141b;
  --ink:#222;
  --text:#444;
  --muted:#777;
  --light:#f3f3f3;
  --line:#e2e2e2;
  --dark:#2b2b2b;
  --footer:#3c3c3c;
  --white:#fff;
}
*{box-sizing:border-box;margin:0;padding:0}
html,body{width:1200px;height:4535px;overflow:hidden}
body{font-family:"Lato",Arial,sans-serif;color:var(--text);background:var(--white);position:relative}
.abs{position:absolute}
section,header,nav,footer{position:absolute;left:0;width:1200px}
.center{text-align:center}

/* top bar */
.topbar{top:0;height:39px;background:var(--red);color:#fff;font-size:11px}
.social{position:absolute;left:108px;top:13px;display:flex;gap:9px}
.social span{width:12px;height:12px;border-radius:50%;background:#fff;opacity:.9}
.topbar .divider{position:absolute;top:0;width:1px;height:39px;background:rgba(255,255,255,.5)}
.address{position:absolute;right:110px;top:13px;display:flex;align-items:center;gap:5px}

/* header */
.masthead{top:39px;height:114px;background:#fff}
.contact{position:absolute;top:34px;display:flex;align-items:center;gap:12px;font-size:14px;color:var(--ink)}
.contact b{display:block;color:var(--red);font-weight:700;margin-top:4px}
.brand{position:absolute;left:500px;top:28px;width:200px;text-align:center;font-size:21px;font-weight:700;color:var(--ink);line-height:1.25}
.brand i{display:inline-block;width:10px;height:10px;background:var(--red);border-radius:50%;margin-right:6px;vertical-align:middle}

/* nav */
.mainnav{top:153px;height:64px;background:var(--light);border-top:1px solid var(--line)}
.mainnav ul{list-style:none;display:flex;justify-content:center;gap:34px;margin-top:20px;font-size:16px;color:var(--ink)}
.mainnav li.active{color:var(--red)}

/* hero */
.hero{top:217px;height:582px;background:linear-gradient(180deg,#7d7f83 0%,#96989c 55%,#b9babd 100%)}
.hero h1{position:absolute;top:198px;width:100%;text-align:center;color:#fff;font-size:40px;font-weight:700;letter-spacing:.5px}
.search{position:absolute;top:279px;left:113px;display:flex;gap:14px}
.field{width:202px;height:48px;background:rgba(60,60,60,.55);color:#eee;font-size:11px;padding:17px 14px;position:relative}
.field svg{position:absolute;right:12px;top:17px}
.btn-search{width:122px;height:48px;background:var(--red);color:#fff;font-size:13px;text-align:center;line-height:48px;margin-left:2px}
.trending{position:absolute;top:364px;width:100%;text-align:center;color:#fff;font-size:12px}
.trending span{font-size:11px}
.browse{position:absolute;top:462px;left:642px;color:#fff;font-size:15px}

.cats{top:723px;height:152px;left:197px;width:806px;display:flex;gap:11px;position:absolute}
.cat{width:153px;height:152px;background:#fff;box-shadow:0 3px 10px rgba(0,0,0,.15);text-align:center;padding-top:18px}
.cat p{color:var(--red);font-size:14px;line-height:1.2;margin-top:6px}
.cat small{display:block;font-size:13px;color:var(--text);margin-top:8px}
.cat.all{background:var(--red);padding:10px}
.cat.all div{border:2px dashed #fff;height:132px;color:#fff;font-size:15px;font-weight:700;display:flex;align-items:center;justify-content:center;line-height:1.5}

/* jobs */
.tabs{position:absolute;top:938px;left:422px;width:354px;height:48px;border:2px solid var(--red);border-radius:24px;display:flex;overflow:hidden;font-size:14px;font-weight:700}
.tabs div{flex:1;text-align:center;line-height:44px;color:var(--red)}
.tabs .on{background:var(--red);color:#fff;border-radius:22px}
.job{position:absolute;width:320px;height:146px;background:#fff;box-shadow:0 2px 8px rgba(0,0,0,.14)}
.job .type{position:absolute;left:8px;top:8px;background:var(--red);color:#fff;font-size:11px;font-weight:700;padding:4px 9px;border-radius:3px}
.job .heart{position:absolute;right:10px;top:10px}
.job .mark{position:absolute;left:14px;top:42px;width:80px;height:80px;background:#f1f1f1;border-radius:4px;display:flex;align-items:center;justify-content:center}
.job .mark span{width:46px;height:46px;border-radius:50%;background:var(--red)}
.job .mark span.g{background:#3aa6a0}
.job .mark span.b{background:#2f7fc1}
.job h3{position:absolute;left:120px;top:36px;font-size:15px;font-weight:400;color:var(--ink)}
.job ul{position:absolute;left:120px;top:66px;list-style:none;font-size:12px;color:var(--ink);line-height:25px}
.job li svg{vertical-align:-1px;margin-right:6px}
.pager{position:absolute;top:1385px;left:484px;display:flex;gap:9px}
.pager span{width:31px;height:30px;background:#555;color:#fff;font-size:13px;text-align:center;line-height:30px}
.pager span.on{background:var(--red)}

/* companies */
.companies{top:1477px;height:626px;background:linear-gradient(180deg,#d8171e,#e42027)}
.companies h2{position:absolute;top:116px;width:100%;text-align:center;color:#fff;font-size:36px;font-weight:400}
.stars{position:absolute;top:60px;left:556px}
.company{position:absolute;top:202px;width:241px;height:311px;background:#fff;text-align:center}
.company .logo{width:78px;height:78px;border-radius:50%;margin:36px auto 0;background:var(--red)}
.company h4{color:var(--red);font-size:15px;font-weight:700;margin-top:28px}
.company p{font-size:13px;color:var(--ink);margin-top:9px}
.company .pill{display:inline-block;margin-top:18px;background:var(--red);color:#fff;font-size:12px;font-weight:700;padding:14px 22px;border-radius:22px}
.dots{position:absolute;top:554px;left:587px;display:flex;gap:4px}
.dots span{width:10px;height:10px;border-radius:50%;border:1px solid #fff}
.dots span.on{background:#fff}

/* how it works */
.how{top:2103px;height:528px;background:#fff}
.how h2{position:absolute;top:52px;width:100%;text-align:center;color:var(--red);font-size:36px;font-weight:400}
.how .sub{position:absolute;top:110px;width:100%;text-align:center;font-size:20px;color:var(--ink)}
.step{position:absolute;top:168px;width:340px;text-align:center}
.step h4{margin-top:22px;color:var(--red);font-size:18px;font-weight:400}
.step p{font-size:12.5px;line-height:25px;color:var(--text);margin:12px auto 0;width:290px}

/* roles */
.roles{top:2631px;height:489px}
.role{position:absolute;top:0;width:600px;height:489px;text-align:center;color:#fff}
.role.emp{left:0;background:linear-gradient(135deg,#c9232a,#a5161c 60%,#d8333a)}
.role.cand{left:600px;background:linear-gradient(135deg,#4d4d4d,#6a6a6a 60%,#3e3e3e)}
.role .im{margin-top:110px;font-size:22px}
.role h2{font-size:44px;font-weight:700;margin-top:14px}
.role p{font-size:15px;line-height:34px;width:430px;margin:16px auto 0}
.role .cta{display:inline-block;margin-top:24px;padding:19px 32px;border-radius:30px;font-size:15px;font-weight:700}
.emp .cta{background:var(--dark)}
.cand .cta{background:var(--red)}

/* advice */
.advice{top:3120px;height:616px;background:#fff}
.advice h2{position:absolute;top:58px;width:100%;text-align:center;color:var(--red);font-size:36px;font-weight:400}
.advice .sub{position:absolute;top:108px;width:100%;text-align:center;font-size:16px;color:var(--ink)}
.post{position:absolute;top:154px;width:329px}
.post .ph{height:193px;background:linear-gradient(135deg,#d9d6d2,#8d8a86)}
.post .tag{position:absolute;left:14px;top:179px;background:var(--red);color:#fff;font-size:14px;padding:8px 20px}
.post .tag.small{font-size:12px;padding:9px 20px}
.post h3{margin-top:42px;color:var(--red);font-size:18px;font-weight:400;line-height:30px}
.post p{margin-top:14px;font-size:11px;line-height:25px;color:var(--text)}
.post a{display:block;margin-top:12px;font-size:12px;color:var(--red);font-weight:700;text-decoration:none}

/* testimonial */
.quotes{top:3736px;height:483px;background:linear-gradient(180deg,#3a3a3a,#4a4a4a);color:#fff;text-align:center}
.quotes h2{margin-top:58px;font-size:36px;font-weight:400}
.quotes .sub{margin-top:12px;font-size:15px}
.quotes .rate{margin-top:36px}
.quotes blockquote{width:800px;margin:26px auto 0;font-size:14px;line-height:31px}
.quotes h4{margin-top:22px;font-size:22px;font-weight:400}
.quotes small{display:block;margin-top:10px;font-size:15px}

/* footer */
.site-foot{top:4219px;height:316px;background:var(--footer);color:#fff}
.foot-brand{position:absolute;left:90px;top:52px;font-size:19px;font-weight:700;color:#fff}
.foot-brand i{display:inline-block;width:10px;height:10px;background:var(--red);border-radius:50%;margin-right:6px;vertical-align:middle}
.foot-about{position:absolute;left:90px;top:170px;width:244px;font-size:11px;line-height:22px;text-align:justify}
.foot-col{position:absolute;top:34px}
.foot-col h5{font-size:21px;font-weight:400}
.foot-col ul{list-style:none;margin-top:28px;font-size:14px;line-height:40px}
.foot-col p{margin-top:24px;font-size:11px;line-height:26px;width:226px;text-align:justify}
.email{margin-top:12px;width:210px;height:38px;background:#fff;color:#aaa;font-size:11px;padding:12px}
.sub-btn{margin-top:14px;width:210px;height:38px;background:var(--red);text-align:center;line-height:38px;font-size:12px;font-weight:700}
.copy{position:absolute;top:4500px;width:100%;text-align:center;font-size:13px;color:#fff}
</style>
</head>
<body>

<header class="topbar">
  <div class="social"><span></span><span></span><span></span><span></span><span></span><span></span><span></span></div>
  <div class="divider" style="left:282px"></div>
  <div class="divider" style="left:773px"></div>
  <div class="address">
    <svg width="9" height="12" viewBox="0 0 10 14"><path d="M5 0a5 5 0 0 0-5 5c0 4 5 9 5 9s5-5 5-9a5 5 0 0 0-5-5zm0 7a2 2 0 1 1 0-4 2 2 0 0 1 0 4z" fill="#fff"/></svg>
    48 Harlow Street, Suite 210, Brookvale, NY 10099
  </div>
</header>

<header class="masthead">
  <div class="contact" style="left:214px">
    <svg width="40" height="40" viewBox="0 0 40 40"><circle cx="20" cy="20" r="18" fill="none" stroke="#ec1c24" stroke-width="2.5"/><path d="M14 12l4 0 2 5-3 2c1 3 3 5 6 6l2-3 5 2v4c-9 1-17-7-16-16z" fill="#ec1c24"/></svg>
    <div>Call us:<b>+1-555-210-0436</b></div>
  </div>
  <div class="brand"><i></i>Talvenhire<br>Network</div>
  <div class="contact" style="left:800px">
    <svg width="40" height="30" viewBox="0 0 40 30"><rect x="1" y="1" width="38" height="28" fill="#ec1c24"/><path d="M1 1l19 15L39 1" fill="none" stroke="#fff" stroke-width="2"/></svg>
    <div>Email us:<b>info@talvenhire.net</b></div>
  </div>
</header>

<nav class="mainnav">
  <ul>
    <li class="active">Home</li><li>Who We Are</li><li>Our Expertise</li><li>Our Services</li><li>Our Blog</li><li>Testimonials</li><li>FAQ's</li><li>Contact Us</li>
  </ul>
</nav>

<section class="hero" role="img" aria-label="Photo of a row of modern shell chairs against a grey wall, one chair in blue">
  <h1>WELCOME TO TALVENHIRE</h1>
  <div class="search">
    <div class="field">Skills</div>
    <div class="field">Salary<svg width="8" height="6"><path d="M0 0h8L4 6z" fill="#fff"/></svg></div>
    <div class="field">All Locations<svg width="12" height="12"><circle cx="6" cy="6" r="4" fill="none" stroke="#fff" stroke-width="1.5"/><circle cx="6" cy="6" r="1.5" fill="#fff"/></svg></div>
    <div class="field">Experience<svg width="12" height="12"><circle cx="6" cy="6" r="5" fill="none" stroke="#fff" stroke-width="1.2"/><path d="M3 6h6" stroke="#fff"/></svg></div>
    <div class="btn-search">Search</div>
  </div>
  <div class="trending">Trending Keywords: <span>Business Analysis, Project Management, Software Development, QA &amp; Testing</span></div>
  <div class="browse">Browse some featured categories</div>
</section>

<div class="cats">
  <div class="cat">
    <svg width="52" height="40" viewBox="0 0 52 40" fill="none" stroke="#ec1c24" stroke-width="2"><rect x="14" y="2" width="36" height="26"/><path d="M20 24v-6M27 24v-10M34 24v-8M41 24v-14"/><circle cx="8" cy="22" r="4"/><path d="M2 38c0-7 3-10 6-10s6 3 6 10"/></svg>
    <p>Business<br>Analysis</p><small>( 10 Profiles )</small>
  </div>
  <div class="cat">
    <svg width="46" height="40" viewBox="0 0 46 40" fill="none" stroke="#ec1c24" stroke-width="2"><path d="M3 14L23 3l20 11z"/><path d="M8 16v18M16 16v18M30 16v18M38 16v18M3 36h40"/></svg>
    <p>Project<br>Management</p><small>( 10 Profiles )</small>
  </div>
  <div class="cat">
    <svg width="48" height="40" viewBox="0 0 48 40" fill="none" stroke="#ec1c24" stroke-width="2"><rect x="4" y="3" width="40" height="26"/><path d="M19 11l-5 5 5 5M29 11l5 5-5 5M26 9l-4 14M16 36h16"/></svg>
    <p>Software<br>Development</p><small>( 10 Profiles )</small>
  </div>
  <div class="cat">
    <svg width="40" height="40" viewBox="0 0 40 40" fill="none" stroke="#ec1c24" stroke-width="2"><path d="M8 16a12 12 0 0 1 24 0z"/><path d="M5 16h30"/><circle cx="20" cy="23" r="6"/><path d="M6 39c0-8 6-11 14-11s14 3 14 11"/></svg>
    <p>QA &amp;<br>Testing</p><small>( 10 Profiles )</small>
  </div>
  <div class="cat all"><div>ALL<br>CATEGORIES</div></div>
</div>

<div class="tabs"><div>RECENT JOBS</div><div class="on">FEATURED JOBS</div></div>

<!-- job cards -->
<div class="job" style="left:88px;top:1024px"><span class="type">Full Time</span><svg class="heart" width="15" height="13" viewBox="0 0 16 14"><path d="M8 14L1 7a4 4 0 0 1 7-5 4 4 0 0 1 7 5z" fill="#ec1c24"/></svg><div class="mark"><span class="g"></span></div><h3>DIGITAL DESIGNER</h3><ul><li><svg width="11" height="9"><rect y="2" width="11" height="7" fill="#333"/><rect x="3" width="5" height="3" fill="none" stroke="#333"/></svg>Brindlecore</li><li><svg width="9" height="12" viewBox="0 0 10 14"><path d="M5 0a5 5 0 0 0-5 5c0 4 5 9 5 9s5-5 5-9a5 5 0 0 0-5-5z" fill="#333"/></svg>New South Wales , Australia</li><li><svg width="10" height="10"><rect width="10" height="10" fill="none" stroke="#333" stroke-width="2"/></svg>1 year ago</li></ul></div>
<div class="job" style="left:439px;top:1024px"><span class="type">Full Time</span><svg class="heart" width="15" height="13" viewBox="0 0 16 14"><path d="M8 14L1 7a4 4 0 0 1 7-5 4 4 0 0 1 7 5z" fill="#ec1c24"/></svg><div class="mark"><span class="b"></span></div><h3>DIGITAL DESIGNER</h3><ul><li><svg width="11" height="9"><rect y="2" width="11" height="7" fill="#333"/><rect x="3" width="5" height="3" fill="none" stroke="#333"/></svg>Brindlecore</li><li><svg width="9" height="12" viewBox="0 0 10 14"><path d="M5 0a5 5 0 0 0-5 5c0 4 5 9 5 9s5-5 5-9a5 5 0 0 0-5-5z" fill="#333"/></svg>New South Wales , Australia</li><li><svg width="10" height="10"><rect width="10" height="10" fill="none" stroke="#333" stroke-width="2"/></svg>1 year ago</li></ul></div>
<div class="job" style="left:790px;top:1024px"><span class="type">Full Time</span><svg class="heart" width="15" height="13" viewBox="0 0 16 14"><path d="M8 14L1 7a4 4 0 0 1 7-5 4 4 0 0 1 7 5z" fill="#ec1c24"/></svg><div class="mark"><span class="b"></span></div><h3>DIGITAL DESIGNER</h3><ul><li><svg width="11" height="9"><rect y="2" width="11" height="7" fill="#333"/><rect x="3" width="5" height="3" fill="none" stroke="#333"/></svg>Brindlecore</li><li><svg width="9" height="12" viewBox="0 0 10 14"><path d="M5 0a5 5 0 0 0-5 5c0 4 5 9 5 9s5-5 5-9a5 5 0 0 0-5-5z" fill="#333"/></svg>New South Wales , Australia</li><li><svg width="10" height="10"><rect width="10" height="10" fill="none" stroke="#333" stroke-width="2"/></svg>1 year ago</li></ul></div>
<div class="job" style="left:88px;top:1204px"><span class="type">Full Time</span><svg class="heart" width="15" height="13" viewBox="0 0 16 14"><path d="M8 14L1 7a4 4 0 0 1 7-5 4 4 0 0 1 7 5z" fill="#ec1c24"/></svg><div class="mark"><span class="b"></span></div><h3>DIGITAL DESIGNER</h3><ul><li><svg width="11" height="9"><rect y="2" width="11" height="7" fill="#333"/><rect x="3" width="5" height="3" fill="none" stroke="#333"/></svg>Brindlecore</li><li><svg width="9" height="12" viewBox="0 0 10 14"><path d="M5 0a5 5 0 0 0-5 5c0 4 5 9 5 9s5-5 5-9a5 5 0 0 0-5-5z" fill="#333"/></svg>New South Wales , Australia</li><li><svg width="10" height="10"><rect width="10" height="10" fill="none" stroke="#333" stroke-width="2"/></svg>1 year ago</li></ul></div>
<div class="job" style="left:439px;top:1204px"><span class="type">Full Time</span><svg class="heart" width="15" height="13" viewBox="0 0 16 14"><path d="M8 14L1 7a4 4 0 0 1 7-5 4 4 0 0 1 7 5z" fill="#ec1c24"/></svg><div class="mark"><span></span></div><h3>DIGITAL DESIGNER</h3><ul><li><svg width="11" height="9"><rect y="2" width="11" height="7" fill="#333"/><rect x="3" width="5" height="3" fill="none" stroke="#333"/></svg>Brindlecore</li><li><svg width="9" height="12" viewBox="0 0 10 14"><path d="M5 0a5 5 0 0 0-5 5c0 4 5 9 5 9s5-5 5-9a5 5 0 0 0-5-5z" fill="#333"/></svg>New South Wales , Australia</li><li><svg width="10" height="10"><rect width="10" height="10" fill="none" stroke="#333" stroke-width="2"/></svg>1 year ago</li></ul></div>
<div class="job" style="left:790px;top:1204px"><span class="type">Full Time</span><svg class="heart" width="15" height="13" viewBox="0 0 16 14"><path d="M8 14L1 7a4 4 0 0 1 7-5 4 4 0 0 1 7 5z" fill="#ec1c24"/></svg><div class="mark"><span class="g"></span></div><h3>DIGITAL DESIGNER</h3><ul><li><svg width="11" height="9"><rect y="2" width="11" height="7" fill="#333"/><rect x="3" width="5" height="3" fill="none" stroke="#333"/></svg>Brindlecore</li><li><svg width="9" height="12" viewBox="0 0 10 14"><path d="M5 0a5 5 0 0 0-5 5c0 4 5 9 5 9s5-5 5-9a5 5 0 0 0-5-5z" fill="#333"/></svg>New South Wales , Australia</li><li><svg width="10" height="10"><rect width="10" height="10" fill="none" stroke="#333" stroke-width="2"/></svg>1 year ago</li></ul></div>

<div class="pager"><span>«</span><span>»</span><span class="on">1</span><span>2</span><span>3</span><span>4</span></div>

<section class="companies" role="img" aria-label="Red-tinted photo of a team seated at a conference table">
  <svg class="stars" width="88" height="30" viewBox="0 0 88 30"><path d="M12 6l3 6 6 1-4.5 4 1 6-5.5-3-5.5 3 1-6L3 13l6-1z" fill="#fff"/><path d="M44 0l4 9 9 1-7 6 2 9-8-5-8 5 2-9-7-6 9-1z" fill="#fff"/><path d="M76 6l3 6 6 1-4.5 4 1 6-5.5-3-5.5 3 1-6-4.5-4 6-1z" fill="#fff"/></svg>
  <h2>TOP COMPANY REGISTERED</h2>
  <div class="company" style="left:92px"><div class="logo"></div><h4>BRINDLECORE</h4><p>Waiting For Love</p><p>United States, Los Angeles</p><span class="pill">4 Open Positions</span></div>
  <div class="company" style="left:350px"><div class="logo" style="background:#2f7fc1"></div><h4>OSTERMARK</h4><p>My Heart Will Go On</p><p>United States, Los Angeles</p><span class="pill">4 Open Positions</span></div>
  <div class="company" style="left:607px"><div class="logo" style="background:#2f7fc1"></div><h4>QUILLFORGE</h4><p>Waiting For Love</p><p>United States, Los Angeles</p><span class="pill">4 Open Positions</span></div>
  <div class="company" style="left:866px"><div class="logo" style="background:#3aa6a0"></div><h4>VELDARION</h4><p>Waiting For Love</p><p>United States, Los Angeles</p><span class="pill">4 Open Positions</span></div>
  <div class="dots"><span></span><span class="on"></span></div>
</section>

<section class="how">
  <h2>HOW IT WORK</h2>
  <div class="sub">Find Jobs, Employment &amp; Career Opportunities</div>
  <svg class="abs" style="left:0;top:150px" width="1200" height="170" viewBox="0 0 1200 170">
    <path d="M320 70C380 10 480 10 520 40" fill="none" stroke="#ec1c24" stroke-dasharray="3 3"/>
    <path d="M690 90C760 160 840 160 890 80" fill="none" stroke="#ec1c24" stroke-dasharray="3 3"/>
    <g fill="none" stroke="#222" stroke-width="2"><circle cx="241" cy="100" r="82"/><path d="M226 182l15 14 15-14"/></g>
    <circle cx="241" cy="100" r="70" fill="#222"/>
    <g fill="none" stroke="#fff" stroke-width="3"><circle cx="234" cy="93" r="20"/><path d="M249 108l20 20"/></g>
    <g fill="none" stroke="#ec1c24" stroke-width="2"><circle cx="604" cy="100" r="82"/><path d="M589 182l15 14 15-14"/></g>
    <circle cx="604" cy="100" r="70" fill="#ec1c24"/>
    <g fill="none" stroke="#fff" stroke-width="2.5"><circle cx="604" cy="86" r="11"/><circle cx="580" cy="96" r="8"/><circle cx="628" cy="96" r="8"/><path d="M586 134v-14a18 18 0 0 1 36 0v14M566 134v-12a14 14 0 0 1 14-14M642 134v-12a14 14 0 0 0-14-14"/></g>
    <g fill="none" stroke="#222" stroke-width="2"><circle cx="970" cy="100" r="82"/><path d="M955 182l15 14 15-14"/></g>
    <circle cx="970" cy="100" r="70" fill="#222"/>
    <g fill="none" stroke="#fff" stroke-width="2.5" stroke-linejoin="round"><path d="M938 100l66-30-20 64-14-22z"/><path d="M970 112l34-42"/></g>
  </svg>
  <div class="step" style="left:71px;top:346px"><h4>REGISTER AN ACCOUNT</h4><p>Post a job to tell us about your project. We'll quickly match you with the right freelancers.</p></div>
  <div class="step" style="left:434px;top:346px"><h4>SPECIFY &amp; SEARCH YOUR JOB</h4><p>Browse profiles, reviews, and proposals then interview top candidates. Hire a favorite and begin your project.</p></div>
  <div class="step" style="left:800px;top:346px"><h4>APPLY FOR JOB</h4><p>Use the Fieldlane platform to chat, share files, and collaborate from your desktop or on the go.</p></div>
</section>

<section class="roles">
  <div class="role emp" role="img" aria-label="Red-toned photo of a smiling businessman writing at a desk">
    <div class="im">I'm an</div><h2>EMPLOYER</h2>
    <p>Signed in companies are able to post new job offers, searching for candidate...</p>
    <span class="cta">&#9679; REGISTER AS COMPANY</span>
  </div>
  <div class="role cand" role="img" aria-label="Dark-toned photo of a cheering group of job seekers">
    <div class="im">I'm an</div><h2>CANDIDATE</h2>
    <p>Browse and search potential candidates for your job that match you, save job....</p>
    <span class="cta">&#9679; REGISTER AS CANDIDATE</span>
  </div>
</section>

<section class="advice">
  <h2>CAREER ADVICE</h2>
  <div class="sub">Etiam imperdiet pulvinar nisl, eu iaculis justo efficitur in.</div>
  <div class="post" style="left:76px"><div class="ph" role="img" aria-label="Photo of colleagues reviewing paperwork at an office desk"></div><span class="tag">OUR BLOG</span><h3>Sed ut perspiciatis unde omnis iste natus error</h3><p>Sed ut perspiciatis unde omnis iste natus error sit voluptatem accusantium doloremque laudantium, totam rem aperiam, eaque ipsa quae ab illo</p><a>READ MORE</a></div>
  <div class="post" style="left:435px"><div class="ph" role="img" aria-label="Photo of a smiling man with glasses in an office"></div><span class="tag small">Dana Whitcomb</span><h3>Sed ut perspiciatis unde omnis iste natus error</h3><p>Sed ut perspiciatis unde omnis iste natus error sit voluptatem accusantium doloremque laudantium, totam rem aperiam, eaque ipsa quae ab illo</p><a>READ MORE</a></div>
  <div class="post" style="left:795px"><div class="ph" role="img" aria-label="Photo of a laughing woman with glasses among colleagues"></div><span class="tag">OUR BLOG</span><h3>Sed ut perspiciatis unde omnis iste natus error</h3><p>Sed ut perspiciatis unde omnis iste natus error sit voluptatem accusantium doloremque laudantium, totam rem aperiam, eaque ipsa quae ab illo</p><a>READ MORE</a></div>
</section>

<section class="quotes" role="img" aria-label="Dark photo backdrop of an office meeting">
  <h2>WHAT CLIENTS SAY?</h2>
  <div class="sub">Read our favorite reviews about our Job Platform from our clients.</div>
  <svg class="rate" width="170" height="24" viewBox="0 0 170 24" fill="#f5a623"><path id="s" d="M12 0l3.5 8 8.5.8-6.4 5.6 1.9 8.4L12 18.5 4.5 22.8l1.9-8.4L0 8.8 8.5 8z"/><use href="#s" x="36"/><use href="#s" x="72"/><use href="#s" x="108"/><use href="#s" x="144"/></svg>
  <blockquote>Sed ut perspiciatis unde omnis iste natus error sit voluptatem accusantium doloremque laudantium, totam rem aperiam, eaque ipsa quae ab illo inventore veritatis et quasi architecto beatae vitae dicta sunt explicabo. Nemo enim ipsam voluptatem quia.</blockquote>
  <h4>Marisol Keane</h4>
  <small>Web designer</small>
</section>

<footer class="site-foot">
  <div class="foot-brand"><i></i>Talvenhire Network</div>
  <p class="foot-about">At vero eos et accusamus et iusto odio dignissimos ducimus qui blanditiis praesentium voluptatum deleniti atque corrupti quos...</p>
  <div class="foot-col" style="left:383px"><h5>FOR CANDIDATES</h5><ul><li>All Jobs</li><li>All Categories</li><li>Companies</li><li>My Account</li></ul></div>
  <div class="foot-col" style="left:643px"><h5>FOR EMPLOYERS</h5><ul><li>All Resums</li><li>All Categories</li><li>All Jobs</li><li>My Account</li></ul></div>
  <div class="foot-col" style="left:885px"><h5>EMAIL NEWSLETTER</h5><p>Subscribe and we'll automatically send you notifications about job matching your personality.</p><div class="email">Email Address</div><div class="sub-btn">SUBSCRIBE</div></div>
</footer>
<div class="copy">Copyrights © 2019. All Rights Reserved.</div>

</body>
</html>
```